Park furniture company needs a new product flyer

We're a street and park furniture supply company and we have a new range of furniture that we would like to showcase to prospective customers.
Pictures, logo and copy attached.
Furniture pictures are also available with a black background.
Warranty information needs to feature on the flyer.
Recycled content information needs to feature on the flyer.

Target Market(s)

Landscape Architects

Font styles to use
Serif

Requirements
Must have
• Professional fonts and graphics.
Should not have
• comic sans or similar fonts - cheap graphics

```html
<!DOCTYPE html>
<html lang="en">
<head>
<meta charset="utf-8">
<title>Kerbline Outdoor – Product Flyer</title>
<link rel="stylesheet" href="https://fonts.googleapis.com/css2?family=Montserrat:wght@300;400;600;700&family=Oswald:wght@500;600&display=swap">
<style>
  :root{
    --page:#d9d9d9;
    --paper:#ffffff;
    --paper-tint:#eef0f2;
    --brand-blue:#2f78c0;
    --brand-red:#c4141a;
    --panel-grey:#5f5f61;
    --logo-grey:#555558;
    --text-white:#ffffff;
    --frame-grey:#b9b9bb;
    --wood:#a8521f;
    --wood-light:#c7783d;
    --metal:#b6a78c;
  }
  *{box-sizing:border-box;margin:0;padding:0}
  html,body{width:1200px;height:1083px;overflow:hidden}
  body{background:var(--page);font-family:"Montserrat",sans-serif;position:relative}

  .flyer{position:absolute;left:230px;top:18px;width:740px;height:1047px;
    background:linear-gradient(160deg,var(--paper-tint),var(--paper) 55%);overflow:hidden;
    box-shadow:0 10px 30px rgba(0,0,0,.18)}

  .brand{position:absolute;left:150px;top:78px;display:flex;align-items:center;gap:14px}
  .brand-mark{width:26px;height:26px;border-radius:50%;background:var(--brand-blue)}
  .brand-name{font-family:"Montserrat",sans-serif;font-weight:700;font-size:44px;
    letter-spacing:1px;color:var(--logo-grey);line-height:1}

  .hero-band{position:absolute;left:0;top:200px;width:560px;height:250px;background:var(--brand-blue)}
  .hero-text{position:absolute;left:40px;top:226px;width:455px;color:var(--text-white);
    font-weight:300;font-size:26px;line-height:1.24;white-space:nowrap}
  .hero-text strong{font-weight:700}

  .warranty-band{position:absolute;left:0;top:450px;width:540px;height:82px;
    background:linear-gradient(90deg,var(--brand-red),#a9161b)}
  .warranty-box{position:absolute;left:40px;top:436px;width:460px;height:104px;
    border:1.5px solid var(--text-white);display:flex;align-items:center;justify-content:center}
  .warranty-text{font-family:"Oswald",sans-serif;font-weight:600;font-size:56px;
    color:var(--text-white);letter-spacing:.5px;white-space:nowrap}

  .hero-product{position:absolute;left:515px;top:170px;width:210px;height:380px;
    background:linear-gradient(150deg,var(--wood-light),var(--wood) 55%,var(--metal));
    clip-path:polygon(40% 0,100% 18%,100% 100%,28% 96%,0 30%)}

  .gallery{position:absolute;left:40px;top:565px;width:220px}
  .gallery-item{width:220px;height:128px;background:var(--paper);border:8px solid var(--frame-grey);
    margin-bottom:14px;box-shadow:0 4px 8px rgba(0,0,0,.15);padding:7px}
  .gallery-photo{width:100%;height:100%;
    background:linear-gradient(160deg,#f2f2f2,#cfc7b8 60%,#8a6a4e)}
  .gallery-photo.bench{background:linear-gradient(160deg,#f2f2f2,#c27a45 55%,#b6a78c)}

  .features{position:absolute;left:290px;top:560px;width:450px;height:370px;
    background:var(--panel-grey);padding:20px 24px 0 30px;color:var(--text-white)}
  .feature-list{list-style:none;position:relative}
  .feature-list::before{content:"";position:absolute;left:9px;top:10px;bottom:10px;
    width:1px;background:rgba(255,255,255,.7)}
  .feature{position:relative;padding-left:32px;font-size:12px;line-height:1.35;margin-bottom:8px}
  .feature svg{position:absolute;left:0;top:-1px;width:19px;height:19px;background:var(--panel-grey)}

  .call-strip{position:absolute;left:280px;top:932px;width:460px;height:50px;display:flex;align-items:center;gap:12px;
    font-family:"Oswald",sans-serif;font-weight:600;color:var(--brand-blue);white-space:nowrap}
  .call-label{font-size:34px}
  .call-number{font-size:40px;letter-spacing:.5px}
  .call-icon{width:42px;height:42px}

  .call-rule{position:absolute;left:280px;top:982px;width:460px;height:8px;background:var(--panel-grey)}
  .web-band{position:absolute;left:0;top:990px;width:740px;height:57px;background:var(--brand-blue);
    display:flex;align-items:center;justify-content:center;gap:12px;white-space:nowrap;
    font-family:"Oswald",sans-serif;font-weight:500;font-size:22px;color:var(--text-white)}
  .web-band svg{width:22px;height:22px}
</style>
</head>
<body>
<main class="flyer">
  <div class="brand">
    <span class="brand-mark"></span>
    <span class="brand-name">Kerbline Outdoor</span>
  </div>

  <div class="hero-band"></div>
  <p class="hero-text">European <strong>inspired</strong><br>with a <strong>unique</strong> and<br><strong>original design</strong>, that is<br>functional all while respecting<br><strong>the Environment.</strong></p>

  <div class="hero-product" role="img" aria-label="Bench with timber-look composite slats, backrest and armrests on a bronze aluminium frame"></div>

  <div class="warranty-band"></div>
  <div class="warranty-box"><span class="warranty-text">10-YEAR WARRANTY</span></div>

  <section class="gallery">
    <div class="gallery-item"><div class="gallery-photo" role="img" aria-label="Picnic table with two bench seats in grey composite slats"></div></div>
    <div class="gallery-item"><div class="gallery-photo bench" role="img" aria-label="Timber-look bench seat with backrest and armrests"></div></div>
    <div class="gallery-item"><div class="gallery-photo" role="img" aria-label="Table and benches setting viewed from an angle"></div></div>
  </section>

  <section class="features">
    <ul class="feature-list">
      <li class="feature"><svg viewBox="0 0 20 20"><circle cx="10" cy="10" r="8.5" fill="none" stroke="#fff" stroke-width="1.5"/><path d="M6 10.2l2.7 2.6L14 7.6" fill="none" stroke="#fff" stroke-width="1.6"/></svg>Our range is designed to make life easier for people; created using extremely durable, ultra low maintenance materials.</li>
      <li class="feature"><svg viewBox="0 0 20 20"><circle cx="10" cy="10" r="8.5" fill="none" stroke="#fff" stroke-width="1.5"/><path d="M6 10.2l2.7 2.6L14 7.6" fill="none" stroke="#fff" stroke-width="1.6"/></svg>Featuring 98% recycled composite battens in a range of stain and fade-resistant colour options and a unique aluminium frame design.</li>
      <li class="feature"><svg viewBox="0 0 20 20"><circle cx="10" cy="10" r="8.5" fill="none" stroke="#fff" stroke-width="1.5"/><path d="M6 10.2l2.7 2.6L14 7.6" fill="none" stroke="#fff" stroke-width="1.6"/></svg>The capped composite battens come with a 10-year commercial warranty covering staining, fading and structural performance.</li>
      <li class="feature"><svg viewBox="0 0 20 20"><circle cx="10" cy="10" r="8.5" fill="none" stroke="#fff" stroke-width="1.5"/><path d="M6 10.2l2.7 2.6L14 7.6" fill="none" stroke="#fff" stroke-width="1.6"/></svg>Site-specific for healthcare applications offering wheelchair accessibility options</li>
      <li class="feature"><svg viewBox="0 0 20 20"><circle cx="10" cy="10" r="8.5" fill="none" stroke="#fff" stroke-width="1.5"/><path d="M6 10.2l2.7 2.6L14 7.6" fill="none" stroke="#fff" stroke-width="1.6"/></svg>The Kerbline Outdoor range comprises of a seat with optional armrests, bench seat and table, available in both standard or DDA designs.</li>
      <li class="feature"><svg viewBox="0 0 20 20"><circle cx="10" cy="10" r="8.5" fill="none" stroke="#fff" stroke-width="1.5"/><path d="M6 10.2l2.7 2.6L14 7.6" fill="none" stroke="#fff" stroke-width="1.6"/></svg>Uniform length of 1800mm with tailored options available.</li>
      <li class="feature"><svg viewBox="0 0 20 20"><circle cx="10" cy="10" r="8.5" fill="none" stroke="#fff" stroke-width="1.5"/><path d="M6 10.2l2.7 2.6L14 7.6" fill="none" stroke="#fff" stroke-width="1.6"/></svg>Bolt down or freestanding options.</li>
    </ul>
  </section>

  <div class="call-strip">
    <span class="call-label">CALL US</span>
    <svg class="call-icon" viewBox="0 0 48 48"><circle cx="24" cy="24" r="21" fill="none" stroke="#2f78c0" stroke-width="3.5"/><path d="M17 13c2-1 3 0 4 2l1.5 3.5c.5 1.2 0 2.2-1 3l-1.3 1c1 2.5 2.8 4.5 5.3 5.8l1-1.3c.8-1 1.9-1.3 3-.8l3.5 1.6c1.8.9 2.6 2 1.6 3.8-1.4 2.5-4 3.4-7 2.3-6-2.2-10.6-7.2-12.4-13.2-.8-2.9.2-5.6 1.8-6.7z" fill="#2f78c0"/></svg>
    <span class="call-number">0198 765 432</span>
  </div>

  <div class="call-rule"></div>
  <div class="web-band">
    <span>FOR MORE INFORMATION VISIT</span>
    <svg viewBox="0 0 26 26" fill="none" stroke="#fff" stroke-width="1.8"><circle cx="13" cy="13" r="11"/><ellipse cx="13" cy="13" rx="5" ry="11"/><path d="M2 13h22M4 7h18M4 19h18"/></svg>
    <span>WWW.KERBLINEOUTDOOR.COM.AU</span>
  </div>
</main>
</body>
</html>
```